Brightwell Electrical and Air conditioning services needs Designer Van Signage.

Brightwell Electrical and Air conditioning company needs a Van signage designed to give customers a professional image of the business. Attached are some sample design that we will be interested in. Do not need full van wrap, Back Half should be ok.

Industry/Entity Type

Electrical, Air conditioning, & Plumbing

Requirements
Must have
• 24 hour emergency service. Electrical , Air conditioning & Plumbing ideas. Please show all around van. front back and 2 sides.
Nice to have
• Please use mobile number: 0437205816, email: info@brightwellelectrical-example.com.au, Web: www.brightwellelectrical-example.com.au.
Should not have
• Full van wrap

```html
<!DOCTYPE html>
<html lang="en">
<head>
<meta charset="utf-8">
<title>Brightwell Van Signage</title>
<link rel="stylesheet" href="https://fonts.googleapis.com/css2?family=Montserrat:wght@500;600;700;800&family=Oswald:wght@600;700&display=swap">
<style>
  :root{
    --bg:#f3f3f3;
    --white:#ffffff;
    --cream:#fdf3ec;
    --orange:#ef9f68;
    --orange-deep:#ee8c4c;
    --red:#e9545c;
    --red-deep:#e2453e;
    --blue:#2b66b1;
    --ink:#222222;
    --edge:#d9d9d9;
  }
  html,body{margin:0;padding:0;overflow:hidden;background:var(--bg);}
  .canvas{width:1200px;height:1151px;display:block;}
  .sans{font-family:"Montserrat",sans-serif;}
  .service{font-family:"Montserrat",sans-serif;font-weight:800;fill:var(--blue);}
  .bullet{fill:var(--red);}
  .brand{font-family:"Montserrat",sans-serif;font-weight:700;}
  .tagline{font-family:"Montserrat",sans-serif;font-weight:700;fill:var(--white);}
  .web{font-family:"Montserrat",sans-serif;font-weight:700;fill:var(--ink);}
  .mail{font-family:"Montserrat",sans-serif;font-weight:500;fill:var(--ink);}
  .phone{font-family:"Montserrat",sans-serif;font-weight:600;fill:var(--white);}
  .badge-num{font-family:"Oswald",sans-serif;font-weight:700;fill:var(--blue);}
  .badge-word{font-family:"Oswald",sans-serif;font-weight:700;fill:var(--blue);}
  .badge-sub{font-family:"Oswald",sans-serif;font-weight:600;fill:var(--white);}
  .licence{font-family:"Montserrat",sans-serif;font-weight:600;fill:var(--ink);}
  .panel-edge{fill:none;stroke:var(--edge);stroke-width:1;}
</style>
</head>
<body>
<svg class="canvas" viewBox="0 0 1200 1151" xmlns="http://www.w3.org/2000/svg" role="img" aria-label="Brightwell van signage: side panel and two rear door options">
  <defs>
    <clipPath id="side-clip"><rect x="190" y="162" width="921" height="309" rx="22"/></clipPath>
    <clipPath id="rear-a-clip"><rect x="145" y="797" width="323" height="150" rx="10"/></clipPath>
    <clipPath id="rear-b-clip"><rect x="742" y="797" width="323" height="150" rx="10"/></clipPath>
  </defs>

  <!-- Side panel -->
  <g class="side-panel" clip-path="url(#side-clip)">
    <rect x="190" y="162" width="921" height="309" fill="var(--white)"/>
    <path class="side-orange" d="M814,162 L1111,162 L1111,471 L545,471 Q660,320 814,162 Z" fill="var(--orange)"/>
    <path class="side-check" d="M364,367 Q440,378 493,424 Q640,262 790,162 L814,162 Q660,320 545,471 L430,471 Q420,410 364,367 Z" fill="var(--red)"/>
    <path class="phone-band" d="M600,439 L820,439 L838,471 L588,471 Z" fill="var(--blue)"/>
  </g>
  <rect class="panel-edge" x="190" y="162" width="921" height="309" rx="22"/>

  <g class="side-small-brand">
    <circle cx="470" cy="340" r="9" fill="var(--orange-deep)"/>
    <text class="brand" x="484" y="370" font-size="15" fill="var(--orange-deep)" text-anchor="middle">Brightwell</text>
    <text class="sans" x="484" y="378" font-size="3.6" font-weight="700" fill="var(--red)" text-anchor="middle">Electrical Air Conditioning Plumbing</text>
  </g>

  <g class="side-main-brand">
    <circle cx="728" cy="300" r="26" fill="none" stroke="var(--white)" stroke-width="7"/>
    <text class="brand" x="728" y="378" font-size="42" fill="var(--white)" text-anchor="middle">Brightwell</text>
    <text class="tagline" x="728" y="390" font-size="9.5" text-anchor="middle">Electrical | Air Conditioning | Plumbing</text>
    <rect x="620" y="398" width="216" height="16" rx="8" fill="none" stroke="var(--blue)" stroke-width="1.3"/>
    <text class="web" x="728" y="409.5" font-size="8" text-anchor="middle">www.brightwellelectrical-example.com.au</text>
    <rect x="659" y="421" width="7" height="5.5" rx="1" fill="none" stroke="var(--blue)" stroke-width="0.9"/>
    <text class="mail" x="669" y="427" font-size="7.4">info@brightwellelectrical-example.com.au</text>
    <circle cx="656" cy="455" r="8.5" fill="var(--orange-deep)"/>
    <path d="M652.5,451 q1,-1 2,0 l1,1.5 q0.3,0.8 -0.6,1.3 q0.8,2 2.6,2.8 q0.6,-0.9 1.3,-0.6 l1.5,1 q1,1 0,2 q-1.5,1.2 -3.5,0 q-3.6,-2.2 -4.8,-5.5 q-0.4,-1.5 0.5,-2.5 z" fill="var(--white)"/>
    <text class="phone" x="669" y="464" font-size="22">0437205816</text>
  </g>

  <g class="side-services">
    <rect class="bullet" x="875" y="205" width="3.5" height="3.5"/>
    <text class="service" x="883" y="216" font-size="16">ELECTRICAL</text>
    <rect class="bullet" x="875" y="232" width="3.5" height="3.5"/>
    <text class="service" x="883" y="243" font-size="16">AIR CONDITIONING</text>
    <rect class="bullet" x="875" y="258" width="3.5" height="3.5"/>
    <text class="service" x="883" y="269" font-size="16">PLUMBING</text>
    <rect class="bullet" x="875" y="282" width="3.5" height="3.5"/>
    <text class="service" x="883" y="293" font-size="16">CCTV SECURITY</text>
  </g>

  <g class="emergency-badge" transform="translate(946,337)">
    <text class="badge-num" x="0" y="32" font-size="34">24/7</text>
    <text class="badge-word" x="67" y="17" font-size="14">Emergency</text>
    <rect x="67" y="21" width="42" height="12" fill="var(--red)"/>
    <text class="badge-sub" x="70" y="31" font-size="9.5">SERVICES</text>
  </g>

  <!-- Rear door option A -->
  <g class="rear-panel-a" clip-path="url(#rear-a-clip)">
    <rect x="145" y="797" width="323" height="150" fill="var(--cream)"/>
    <path d="M145,797 L447,797 Q360,850 312,947 L145,947 Z" fill="var(--orange-deep)"/>
    <path d="M236,891 Q268,898 288,920 Q360,840 447,797 L468,797 L468,800 Q380,850 312,947 L270,947 Q262,912 236,891 Z" fill="var(--red-deep)"/>
    <path d="M145,923 L260,923 L268,937 L145,937 Z" fill="var(--red-deep)"/>
  </g>
  <rect class="panel-edge" x="145" y="797" width="323" height="150" rx="10"/>
  <g class="rear-a-text">
    <g fill="var(--red)"><circle cx="155" cy="850" r="1"/><circle cx="155" cy="864" r="1"/><circle cx="155" cy="878" r="1"/><circle cx="155" cy="891" r="1"/></g>
    <g class="service" font-size="8.5">
      <text x="158" y="853">ELECTRICAL</text>
      <text x="158" y="867">AIR CONDITIONING</text>
      <text x="158" y="881">PLUMBING</text>
      <text x="158" y="894">CCTV SECURITY</text>
    </g>
    <text class="licence" x="161" y="918" font-size="4.4">Electrical License Number - EL482913</text>
    <circle cx="161" cy="930" r="7" fill="var(--blue)" stroke="var(--white)" stroke-width="1"/>
    <text class="phone" x="176" y="935" font-size="13">0437205816</text>
  </g>
  <g class="emergency-badge" transform="translate(335,897)">
    <text class="badge-num" x="0" y="30" font-size="31">24/7</text>
    <text class="badge-word" x="64" y="16" font-size="13">Emergency</text>
    <rect x="64" y="20" width="37" height="11" fill="var(--red)"/>
    <text class="badge-sub" x="67" y="29" font-size="8.5">SERVICES</text>
  </g>

  <!-- Rear door option B -->
  <g class="rear-panel-b" clip-path="url(#rear-b-clip)">
    <rect x="742" y="797" width="323" height="150" fill="var(--white)"/>
    <path d="M1044,797 L1065,797 L1065,947 L909,947 Q960,850 1044,797 Z" fill="var(--orange-deep)"/>
    <path d="M833,891 Q865,898 885,920 Q957,840 1044,797 L1065,797 L1065,800 Q977,850 909,947 L867,947 Q859,912 833,891 Z" fill="var(--red)"/>
    <path d="M742,923 L857,923 L865,937 L742,937 Z" fill="var(--blue)"/>
  </g>
  <rect class="panel-edge" x="742" y="797" width="323" height="150" rx="10"/>
  <g class="rear-b-text">
    <g fill="var(--red)"><circle cx="752" cy="850" r="1"/><circle cx="752" cy="864" r="1"/><circle cx="752" cy="878" r="1"/><circle cx="752" cy="891" r="1"/></g>
    <g class="service" font-size="8.5">
      <text x="755" y="853">ELECTRICAL</text>
      <text x="755" y="867">AIR CONDITIONING</text>
      <text x="755" y="881">PLUMBING</text>
      <text x="755" y="894">CCTV SECURITY</text>
    </g>
    <text class="licence" x="759" y="918" font-size="4.4">Electrical License Number - EL482913</text>
    <circle cx="759" cy="930" r="7" fill="var(--orange-deep)" stroke="var(--white)" stroke-width="1"/>
    <text class="phone" x="774" y="935" font-size="13">0437205816</text>
  </g>
  <g class="emergency-badge" transform="translate(933,897)">
    <text class="badge-num" x="0" y="30" font-size="31">24/7</text>
    <text class="badge-word" x="64" y="16" font-size="13">Emergency</text>
    <rect x="64" y="20" width="37" height="11" fill="var(--red)"/>
    <text class="badge-sub" x="67" y="29" font-size="8.5">SERVICES</text>
  </g>
</svg>
</body>
</html>
```